Flair Bartenders Website Needs an Overhaul

We are a group of flair bartenders based in San Diego that provide a fun bartending alternative to private parties and events. We haven’t changed our website design in a long time and need to bring our current flash based website in line with the times and go to HTML5 (see our website www.twirlmaniaks.com).

We have a “skateboard grunge” theme to our current website and would like to keep that look as our pictures and video are all taken in an urban setting. We are not married to any particular colors and want to have a “rock star” feel to the site as it needs to attract people that like to party!

Find in the files our logo and the font file.

Target Market(s)

Our clients are fun, outgoing individuals where normal lines are blurred and risks are taken.

Industry/Entity Type

Events

Number of Pages Required

4 page

Requirements
Must have
• An urban skateboarding feel.
Nice to have
• Keep the green theme, although not essential.
Should not have
• No "business type" "corporate" websites.. BORING!!

```html
<!DOCTYPE html>
<html lang="en">
<head>
<meta charset="utf-8">
<title>Twirlmaniaks – Flair Bartenders San Diego</title>
<link rel="stylesheet" href="https://fonts.googleapis.com/css2?family=Raleway:wght@500;600;700;800&family=Open+Sans:wght@400;600&family=Tinos:wght@400&display=swap">
<style>
  :root {
    --grunge-top: #333333;
    --grunge-mid: #1c1c1c;
    --nav-light: #f4f4f4;
    --nav-shade: #d4d4d4;
    --nav-active: #0b0b0b;
    --text-dark: #2a2a2a;
    --text-body: #4a4a4a;
    --text-light: #f1f1f1;
    --muted: #9a9a9a;
    --orange: #f39a1c;
    --lime: #9cc43a;
    --teal: #25c98f;
    --button-top: #ffa41c;
    --button-bottom: #f07e00;
    --footer: #161616;
  }
  * { box-sizing: border-box; margin: 0; padding: 0; }
  html, body { width: 1200px; height: 1158px; overflow: hidden; }
  body {
    position: relative;
    background: var(--footer);
    font-family: "Open Sans", sans-serif;
    color: var(--text-body);
  }

  /* grunge masthead */
  .masthead-bg {
    position: absolute; left: 0; top: 0; width: 1200px; height: 600px;
    background: radial-gradient(ellipse at 45% 25%, var(--grunge-top), var(--grunge-mid) 75%);
  }
  .masthead-bg::before {
    content: ""; position: absolute; left: 0; top: 0; width: 1200px; height: 8px;
    background: #3a3a3a;
  }
  .masthead-photo {
    position: absolute; left: 0; top: 8px; width: 210px; height: 552px;
    background: linear-gradient(90deg, #444 0%, #333 55%, rgba(40,40,40,0) 100%);
  }
  .grain { position: absolute; left: 0; pointer-events: none; }
  .grain-top { top: 0; }
  .grain-welcome { top: 800px; }
  .masthead-curve { position: absolute; left: 0; top: 500px; width: 1200px; height: 120px; }

  .brand {
    position: absolute; left: 191px; top: 48px;
    font-family: "Raleway", sans-serif; font-weight: 800; font-size: 46px;
    color: #ffffff; letter-spacing: -0.5px; line-height: 1;
  }
  .enquiry {
    position: absolute; right: 195px; top: 78px; text-align: right;
    font-family: "Raleway", sans-serif;
  }
  .enquiry-label { font-size: 15px; font-weight: 500; color: var(--muted); letter-spacing: 0.3px; }
  .enquiry-phone {
    display: flex; align-items: center; gap: 2px; justify-content: flex-end;
    font-family: "Open Sans", sans-serif; font-size: 23px; color: #ffffff; margin-top: 1px;
  }

  .main-nav {
    position: absolute; left: 192px; top: 135px; width: 816px; height: 45px;
    display: flex; background: linear-gradient(var(--nav-light), var(--nav-shade));
  }
  .main-nav a {
    display: flex; align-items: center; justify-content: center;
    font-family: "Tinos", serif; font-size: 14px; color: #111;
    text-decoration: none; border-right: 1px solid #b8b8b8;
  }
  .main-nav a:last-child { border-right: none; }
  .main-nav a.is-active { background: var(--nav-active); color: #fff; }

  .hero-shadow {
    position: absolute; left: 180px; top: 570px; width: 840px; height: 26px;
    background: radial-gradient(ellipse at 50% 30%, rgba(0,0,0,0.35), rgba(0,0,0,0) 70%);
  }
  .hero {
    position: absolute; left: 192px; top: 180px; width: 816px; height: 405px;
    background: linear-gradient(120deg, #2a1a12 0%, #5c3e2a 30%, #c9c2b8 50%, #8a5630 68%, #2b1a12 100%);
    clip-path: polygon(0 0, 816px 0,
      813px 30px, 816px 60px, 812px 90px, 815px 120px, 811px 150px, 816px 180px, 812px 210px, 815px 240px, 811px 270px, 816px 300px, 812px 330px, 815px 360px, 811px 385px, 816px 398px,
      800px 398px, 784px 404px, 768px 401px, 752px 405px, 736px 397px, 720px 403px, 704px 400px, 688px 405px, 672px 398px, 656px 404px, 640px 401px, 624px 405px, 608px 397px, 592px 403px, 576px 400px, 560px 405px, 544px 398px, 528px 404px, 512px 401px, 496px 405px, 480px 397px, 464px 403px, 448px 400px, 432px 405px, 416px 398px, 400px 404px, 384px 401px, 368px 405px, 352px 397px, 336px 403px, 320px 400px, 304px 405px, 288px 398px, 272px 404px, 256px 401px, 240px 405px, 224px 397px, 208px 403px, 192px 400px, 176px 405px, 160px 398px, 144px 404px, 128px 401px, 112px 405px, 96px 397px, 80px 403px, 64px 400px, 48px 405px, 32px 398px, 16px 403px, 0 397px,
      4px 380px, 1px 360px, 4px 330px, 0 300px, 3px 270px, 0 240px, 2px 210px, 0 180px, 4px 150px, 1px 120px, 3px 90px, 0 60px, 2px 30px);
  }
  .hero-edge { position: absolute; left: 0; top: 0; width: 816px; height: 405px; }
  .hero-dots {
    position: absolute; left: 50%; bottom: 20px; transform: translateX(-50%);
    display: flex; gap: 6px;
  }
  .hero-dots span { width: 12px; height: 12px; border-radius: 50%; background: #2a2a2a; }

  /* feature teasers */
  .features {
    position: absolute; left: 0; top: 600px; width: 1200px; height: 200px;
    background: linear-gradient(#ffffff, #e4e4e4);
  }
  .feature { position: absolute; top: 36px; }
  .feature h2 {
    font-family: "Raleway", sans-serif; font-weight: 700; font-size: 18px; line-height: 1;
    margin-bottom: 7px; white-space: nowrap;
  }
  .feature p { font-size: 9.4px; line-height: 14px; color: var(--text-body); padding-left: 2px; white-space: nowrap; }
  .feature .more {
    display: flex; align-items: center; gap: 5px; margin-top: 11px; padding-left: 3px;
    font-family: "Raleway", sans-serif; font-weight: 600; font-size: 12.5px; color: var(--text-dark);
  }
  .feature-crew { left: 190px; } .feature-crew h2 { color: var(--orange); }
  .feature-packages { left: 472px; } .feature-packages h2 { color: var(--lime); }
  .feature-flair { left: 757px; } .feature-flair h2 { color: var(--teal); }

  /* welcome */
  .welcome {
    position: absolute; left: 0; top: 800px; width: 1200px; height: 263px;
    background: radial-gradient(ellipse at 50% 40%, #2a2a2a, #131313 75%);
  }
  .welcome-copy { position: absolute; left: 190px; top: 52px; color: var(--text-light); z-index: 2; }
  .welcome-copy h1 {
    font-family: "Raleway", sans-serif; font-weight: 500; font-size: 24px; color: #fff;
    margin-bottom: 12px;
  }
  .welcome-copy p { font-size: 9.8px; line-height: 14px; margin-bottom: 7px; white-space: nowrap; }
  .read-more {
    display: inline-block; margin-top: 5px; padding: 7px 16px;
    background: linear-gradient(var(--button-top), var(--button-bottom));
    border-radius: 3px; font-family: "Raleway", sans-serif; font-weight: 600;
    font-size: 10px; color: #fff; text-decoration: none;
  }
  .video {
    position: absolute; left: 735px; top: 41px; width: 271px; height: 173px;
    border: 3px solid #fff; z-index: 2;
    background: linear-gradient(135deg, #9aa0a8, #6e5a52 45%, #2a2320 80%);
  }
  .video-play {
    position: absolute; left: 50%; top: 50%; width: 34px; height: 34px;
    margin: -17px 0 0 -17px;
  }

  /* footer */
  .site-footer { position: absolute; left: 0; top: 1063px; width: 1200px; height: 95px; background: var(--footer); border-top: 1px solid #242424; }
  .footer-nav {
    position: absolute; left: 195px; top: 29px; display: flex; gap: 6px;
    font-family: "Raleway", sans-serif; font-weight: 500; font-size: 12.5px; color: #fff;
  }
  .footer-nav .sep { color: #ccc; }
  .legal { position: absolute; left: 196px; top: 52px; font-size: 10px; color: var(--muted); }
  .social { position: absolute; right: 204px; top: 28px; display: flex; gap: 9px; }
  .social span { width: 16px; height: 16px; border-radius: 50%; background: #fff; }
</style>
</head>
<body>
  <div class="masthead-bg"></div>
  <div class="masthead-photo" role="img" aria-label="Faded black and white photo of a bartender tossing a bottle"></div>
  <svg class="grain grain-top" width="1200" height="600" aria-hidden="true">
    <filter id="grit">
      <feTurbulence type="fractalNoise" baseFrequency="0.85" numOctaves="2" seed="4"/>
      <feColorMatrix values="0 0 0 0 1  0 0 0 0 1  0 0 0 0 1  0 0 0 1.2 -0.55"/>
    </filter>
    <filter id="stain">
      <feTurbulence type="fractalNoise" baseFrequency="0.012 0.02" numOctaves="5" seed="9"/>
      <feColorMatrix values="0 0 0 0 0  0 0 0 0 0  0 0 0 0 0  0 0 0 2.2 -1.0"/>
    </filter>
    <rect width="1200" height="600" filter="url(#stain)" opacity="0.55"/>
    <rect width="1200" height="600" filter="url(#grit)" opacity="0.14"/>
  </svg>
  <svg class="masthead-curve" viewBox="0 0 1200 120" preserveAspectRatio="none" aria-hidden="true">
    <polygon points="0,72 192,24 192,120 0,120" fill="#ffffff"/>
    <polygon points="0,58 192,16 192,24 0,72" fill="#5a5a5a"/>
    <polygon points="1008,36 1200,72 1200,120 1008,120" fill="#ffffff"/>
    <polygon points="1008,28 1200,58 1200,72 1008,36" fill="#5a5a5a"/>
    <rect x="192" y="85" width="816" height="35" fill="#ffffff"/>
  </svg>

  <header>
    <div class="brand">Twirlmaniaks</div>
    <div class="enquiry">
      <div class="enquiry-label">FOR ENQUIRY</div>
      <div class="enquiry-phone">
        <svg width="18" height="18" viewBox="0 0 24 24" aria-hidden="true"><path fill="#fff" d="M6.6 10.8a15.1 15.1 0 0 0 6.6 6.6l2.2-2.2c.3-.3.7-.4 1-.2 1.1.4 2.3.6 3.6.6.6 0 1 .4 1 1V20c0 .6-.4 1-1 1C10.6 21 3 13.4 3 4c0-.6.4-1 1-1h3.5c.6 0 1 .4 1 1 0 1.3.2 2.5.6 3.6.1.3 0 .7-.2 1z"/></svg>
        <span>1.619.555.0147</span>
      </div>
    </div>
    <nav class="main-nav">
      <a class="is-active" style="width:95px">HOME</a>
      <a style="width:109px">ABOUT US</a>
      <a style="width:103px">BOOKING</a>
      <a style="width:112px">PACKAGES</a>
      <a style="width:82px">CREW</a>
      <a style="width:86px">MEDIA</a>
      <a style="width:109px">FAN CLUB</a>
      <a style="width:120px">CONTACT</a>
    </nav>
  </header>

  <div class="hero-shadow"></div>
  <section class="hero" role="img" aria-label="Smiling bartender in bow tie and suspenders giving a thumbs up behind a bar">
    <svg class="hero-edge" viewBox="0 0 816 405" aria-hidden="true">
      <polyline points="0,397 16,403 32,398 48,405 64,400 80,403 96,397 112,405 128,401 144,404 160,398 176,405 192,400 208,403 224,397 240,405 256,401 272,404 288,398 304,405 320,400 336,403 352,397 368,405 384,401 400,404 416,398 432,405 448,400 464,403 480,397 496,405 512,401 528,404 544,398 560,405 576,400 592,403 608,397 624,405 640,401 656,404 672,398 688,405 704,400 720,403 736,397 752,405 768,401 784,404 800,398 816,398" fill="none" stroke="#111" stroke-width="5"/>
      <polyline points="2,30 0,60 3,90 1,120 4,150 0,180 2,210 0,240 3,270 0,300 4,330 1,360 4,380 0,397" fill="none" stroke="#111" stroke-width="5"/>
      <polyline points="813,30 816,60 812,90 815,120 811,150 816,180 812,210 815,240 811,270 816,300 812,330 815,360 811,385 816,398" fill="none" stroke="#111" stroke-width="5"/>
    </svg>
    <div class="hero-dots"><span></span><span></span><span></span><span></span></div>
  </section>

  <section class="features">
    <article class="feature feature-crew">
      <h2>OUR CREW</h2>
      <p>In massa libero interdum nec interdum vel blandit sed<br>nulla In ullamcorper est eget tempor cursus neque<br>mi consectetuer mi a ultricies massa est sed nisl Class<br>aptent taciti ad litora torq</p>
      <div class="more">CLICK HERE <svg width="6" height="10" viewBox="0 0 6 10"><path d="M1 1l4 4-4 4" stroke="#999" fill="none"/></svg></div>
    </article>
    <article class="feature feature-packages">
      <h2>OUR PACKAGES</h2>
      <p>In massa libero interdum nec interdum vel blandit sed<br>nulla In ullamcorper est eget tempor cursus neque<br>mi consectetuer mi a ultricies massa est sed nisl Class<br>aptent taciti ad litora torq</p>
      <div class="more">CLICK HERE <svg width="6" height="10" viewBox="0 0 6 10"><path d="M1 1l4 4-4 4" stroke="#999" fill="none"/></svg></div>
    </article>
    <article class="feature feature-flair">
      <h2>WHAT IS EXHIBITION FLAIR?</h2>
      <p>In massa libero interdum nec interdum vel blandit sed<br>nulla In ullamcorper est eget tempor cursus neque<br>mi consectetuer mi a ultricies massa est sed nisl Class<br>aptent taciti ad litora torq</p>
      <div class="more">CLICK HERE <svg width="6" height="10" viewBox="0 0 6 10"><path d="M1 1l4 4-4 4" stroke="#999" fill="none"/></svg></div>
    </article>
  </section>

  <section class="welcome">
    <svg class="grain" style="top:0" width="1200" height="263" aria-hidden="true">
      <rect width="1200" height="263" filter="url(#stain)" opacity="0.5"/>
      <rect width="1200" height="263" filter="url(#grit)" opacity="0.1"/>
    </svg>
    <div class="welcome-copy">
      <h1>Welcome to Twirlmaniaks Mainpage</h1>
      <p>The Twirlmaniaks are San Diego’s top flair bartenders brought to your event and blended together with a dedication<br>to service, mixology and entertainment. This is a fun alternative to traditional bartending that still provides great<br>service with specialized personal crowd interaction plus an unbelievable flair show.</p>
      <p>Audiences are very receptive to this practical form of entertainment and it blends well in conjunction with live<br>bands, DJs and fun events. The working package is most commonly requested with our bookings, and highly<br>practical for both service and entertainment</p>
      <a class="read-more">READ MORE</a>
    </div>
    <div class="video" role="img" aria-label="Video still of a bartender balancing a bottle on his arm">
      <svg class="video-play" viewBox="0 0 34 34" aria-hidden="true"><circle cx="17" cy="17" r="17" fill="#fff"/><path d="M13 10l11 7-11 7z" fill="#111"/></svg>
    </div>
  </section>

  <footer class="site-footer">
    <nav class="footer-nav">
      <span>HOME</span><span class="sep">|</span><span>ABOUT US</span><span class="sep">|</span><span>BOOKING</span><span class="sep">|</span><span>PACKAGES</span><span class="sep">|</span><span>CREW</span><span class="sep">|</span><span>MEDIA</span><span class="sep">|</span><span>FAN CLUB</span><span class="sep">|</span><span>CONTACT</span>
    </nav>
    <div class="legal">© 2015 Company Name&nbsp; All right reserved&nbsp; Term of Use</div>
    <div class="social" aria-label="Social links"><span></span><span></span><span></span></div>
  </footer>
</body>
</html>
```